Website for our 3rd party logistics warehouse company

Our company is a 3rd party logistics company. We receive and ship other businesses products for them. We offer our services to other smaller businesses that do not have a warehouse to operate out of. We also help many Brindlemart businesses prepare their products to be sold on Brindlemart.

We are looking for a modern looking design for our website. Please see our attached logo for design ideas. We are open to changing logo colors for website.

We really like the look of the website www.quorvane.com

Target Market(s)

Other businesses and brands of products

Industry/Entity Type

Warehousing and shipping

Number of Pages Required

2 page

Requirements
Must have
• We need 2 pages. Our main landing page and a duplicate page with different information geared towards brands.
Nice to have
• I like the look of overlay/transparent sections. Please see quorvane.com there is a ribbon that shows "Partners".

```html
<!DOCTYPE html>
<html lang="en">
<head>
<meta charset="utf-8">
<title>Orbitline 3PL – Receive, Prep and Ship</title>
<link rel="stylesheet" href="https://fonts.googleapis.com/css2?family=Poppins:wght@300;400;500;600;700&display=swap">
<style>
:root{
  --yellow:#f5bf26;
  --yellow-deep:#eeb320;
  --navy:#1c1e2b;
  --navy-soft:#262937;
  --ink:#2a2a2a;
  --grey:#6b6b6b;
  --grey-light:#9a9a9a;
  --paper:#ffffff;
  --mist:#f6f6f7;
  --badge:#d9dade;
}
*{margin:0;padding:0;box-sizing:border-box}
html,body{width:1200px;height:4819px;overflow:hidden}
body{font-family:"Poppins",sans-serif;color:var(--ink);background:var(--paper);position:relative}
.abs{position:absolute}
.accent{color:var(--yellow)}
.section-title{position:absolute;font-size:28px;font-weight:500;color:var(--grey-light)}
.section-title .accent{color:var(--yellow)}
.rule{position:absolute;height:3px;width:46px;background:var(--yellow)}
.rule::after{content:"";position:absolute;left:52px;top:0;width:8px;height:3px;background:var(--navy)}
.btn{position:absolute;display:flex;align-items:center;justify-content:center;border-radius:22px;font-size:14px;font-weight:600;text-transform:uppercase;color:var(--navy);background:var(--yellow)}
.ph{position:absolute}

/* top bar */
.topbar{left:0;top:0;width:1200px;height:33px}
.topbar-bg{position:absolute;left:0;top:0}
.topbar-text{position:absolute;top:9px;font-size:11px;color:var(--navy);white-space:nowrap}
.topbar-text.big{font-size:14px;top:6px}

/* hero */
.hero{left:0;top:0;width:1200px;height:720px;overflow:hidden}
.brand{position:absolute;font-weight:600;letter-spacing:3px;color:#fff}
.hero-title{left:618px;top:206px;font-size:41px;line-height:46px;font-weight:600;color:#fff}
.hero-copy{left:621px;top:364px;width:420px;font-size:12.5px;line-height:21px;color:#fff}
.hero-arrow{position:absolute;width:40px;height:40px;border:2px solid rgba(255,255,255,.8);border-radius:50%}

/* who */
.who-copy{left:370px;top:852px;width:460px;text-align:center;font-size:12px;line-height:23px;color:var(--grey)}
.partner{position:absolute;top:949px;width:180px;height:75px;background:#fff;box-shadow:0 2px 8px rgba(0,0,0,.12);display:flex;align-items:center;justify-content:center}
.partner-name{font-size:22px;font-weight:700;color:var(--navy)}
.partner-badge{width:110px;height:28px;border-radius:4px;background:var(--badge)}

/* why dark */
.why-list{left:152px;top:1300px;width:420px;list-style:none}
.why-list li{position:relative;padding-left:45px;font-size:12px;line-height:21px;color:#c9cad1;margin-bottom:17px}
.why-list li::before{content:"";position:absolute;left:4px;top:5px;width:12px;height:12px;border:2px solid var(--yellow);border-radius:50%}
.orbit-label{position:absolute;font-size:14px;line-height:19px;color:var(--yellow);text-align:center}

/* features yellow */
.feature-icon{position:absolute;width:76px;height:76px;border-radius:50%;background:#fff;box-shadow:0 0 0 6px rgba(255,255,255,.35);display:flex;align-items:center;justify-content:center}
.feature-text{position:absolute;font-size:12.5px;line-height:21px;font-weight:500;color:var(--navy)}

/* software */
.software-copy{left:680px;top:2326px;width:380px;font-size:12px;line-height:23px;color:var(--grey)}
.shot{position:absolute;background:#fff;box-shadow:0 2px 6px rgba(0,0,0,.15)}
.shot-side{position:absolute;left:0;top:0;bottom:0;width:36px;background:var(--navy-soft)}

/* pricing */
.price-card{left:586px;top:2789px;width:419px;height:412px;background:#fff;box-shadow:0 3px 14px rgba(0,0,0,.14)}
.price-row{position:absolute;left:0;width:419px;height:42px;display:flex;align-items:center;padding:0 22px 0 42px;font-size:13px;color:var(--ink)}
.price-row:nth-child(even){background:var(--mist)}
.price-row::before{content:"";position:absolute;left:22px;top:18px;width:6px;height:6px;border-radius:50%;background:var(--yellow)}
.price-row .amt{margin-left:auto;color:var(--yellow);font-size:17px;font-weight:500}
.pricing-lead{left:138px;top:2930px;font-size:31px;line-height:35px;font-weight:600;color:var(--yellow)}
.pricing-sub{left:138px;top:3010px;width:320px;font-size:12.5px;line-height:22px;color:var(--grey)}

/* guarantee */
.guarantee-copy{left:124px;top:3395px;width:400px;font-size:12.5px;line-height:22px;color:var(--grey)}
.guarantee-big{left:124px;top:3515px;font-size:43px;line-height:53px;font-weight:700;color:var(--yellow);-webkit-text-stroke:1.2px #b58a10}
.guarantee-big .muted{color:#d6d6d6;-webkit-text-stroke:1.2px #9a9a9a}
.guarantee-note{left:128px;top:3628px;font-size:19px;font-weight:500;color:var(--navy)}

/* contact */
.contact-sub{left:0;top:3968px;width:1200px;text-align:center;font-size:13px;color:var(--navy)}
.field{position:absolute;height:40px;background:#fff;border-radius:6px;padding:11px 14px;font-size:11px;color:var(--grey)}
.field.select::after{content:"";position:absolute;right:14px;top:17px;border:5px solid transparent;border-top-color:var(--ink)}

/* footer */
.contact-item{position:absolute;top:4528px;display:flex;gap:18px;align-items:flex-start}
.contact-ring{width:50px;height:50px;border-radius:50%;background:var(--yellow);box-shadow:0 0 0 5px rgba(245,191,38,.25);display:flex;align-items:center;justify-content:center;flex:none}
.contact-lines{font-size:11px;line-height:17px;color:#fff;padding-top:2px}
.contact-lines span{display:block;color:#a8aab4}
.copyright{left:0;top:4633px;width:1200px;text-align:center;font-size:11px;color:#c9cad1}
.disclaimer-title{left:0;top:4703px;width:1200px;text-align:center;font-size:12px;color:var(--yellow)}
.disclaimer{left:60px;top:4730px;width:1080px;text-align:center;font-size:9.5px;line-height:19px;color:#c9cad1}
</style>
</head>
<body>

<!-- HERO -->
<section class="abs hero">
  <div class="ph" role="img" aria-label="Courier with a yellow delivery backpack cycling through a city street" style="left:0;top:0;width:1200px;height:720px;background:linear-gradient(100deg,#5d5f63 0%,#8d8c88 35%,#a9a7a2 60%,#6f7073 100%)"></div>
  <div class="abs" style="left:0;top:0;width:1200px;height:720px;background:linear-gradient(90deg,rgba(0,0,0,.15),rgba(0,0,0,.35))"></div>
  <svg class="abs" style="left:0;top:0" width="1200" height="720" viewBox="0 0 1200 720">
    <path d="M0 640 C 260 720 520 720 760 640 C 930 585 1080 545 1200 520 L1200 720 L0 720 Z" fill="#fff"/>
    <path d="M1200 505 C 1060 535 940 570 800 620 C 960 590 1080 560 1200 548 Z" fill="#b9b9bb"/>
    <path d="M1200 510 C 1120 525 1040 545 960 570 C 1060 552 1140 540 1200 536 Z" fill="var(--yellow)"/>
    <path d="M0 640 C 120 690 240 712 380 716 C 230 700 110 675 0 620 Z" fill="var(--yellow)"/>
  </svg>
  <div class="brand" style="left:67px;top:55px;font-size:20px">ORBITLINE 3PL</div>
  <svg class="abs" style="left:1096px;top:58px" width="44" height="26"><g fill="var(--yellow)"><rect width="44" height="3" y="0"/><rect width="44" height="3" y="10"/><rect width="44" height="3" y="20"/></g></svg>
  <div class="hero-arrow" style="left:60px;top:321px"><svg width="36" height="36"><path d="M21 11 L14 18 L21 25" stroke="#fff" stroke-width="1.5" fill="none"/></svg></div>
  <div class="hero-arrow" style="left:1098px;top:321px"><svg width="36" height="36"><path d="M15 11 L22 18 L15 25" stroke="#fff" stroke-width="1.5" fill="none"/></svg></div>
  <h1 class="abs hero-title">We <span class="accent">Receive And Ship</span><br>Other Businesses<br>Products for Them</h1>
  <p class="abs hero-copy">We Offer our Services to Other Smaller Businesses that do not Have a Warehouse To Operate out of</p>
  <div class="btn" style="left:621px;top:426px;width:188px;height:38px;font-size:13px">Request a Quote</div>
</section>

<!-- TOP BAR -->
<div class="abs topbar">
  <svg class="topbar-bg" width="1200" height="33"><path d="M540 0 H1200 V33 H560 Z" fill="var(--yellow)"/></svg>
  <div class="topbar-text" style="left:571px">We Are Available For You 24 x 7 :</div>
  <svg class="abs" style="left:772px;top:5px" width="24" height="24"><circle cx="12" cy="12" r="12" fill="var(--navy)"/><path d="M8 7 l3 0 1 3 -2 1 a7 7 0 0 0 3 3 l1 -2 3 1 0 3 a9 9 0 0 1 -9 -9z" fill="#fff"/></svg>
  <div class="topbar-text big" style="left:808px">+1 000 000 0000</div>
  <svg class="abs" style="left:965px;top:5px" width="24" height="24"><circle cx="12" cy="12" r="12" fill="var(--navy)"/><rect x="6" y="8" width="12" height="8" fill="#fff"/><path d="M6 8 L12 13 L18 8" stroke="var(--navy)" fill="none"/></svg>
  <div class="topbar-text big" style="left:1000px">info@orbitline3pl.com</div>
</div>

<!-- WHO WE ARE -->
<h2 class="section-title" style="left:0;width:1200px;text-align:center;top:774px">Who <span class="accent">We Are</span></h2>
<p class="abs who-copy">Orbitline 3PL is your one stop 3PL that will help you grow your business and allow you to be hands off. We offer high end services and meet our commitment, guaranteed</p>
<div class="partner" style="left:206px"><span class="partner-name">brindlemart</span></div>
<div class="partner" style="left:400px"><div class="partner-badge"></div></div>
<div class="partner" style="left:595px"><div class="partner-badge"></div></div>
<div class="partner" style="left:789px"><div class="partner-badge"></div></div>

<!-- WHY (DARK) -->
<svg class="abs" style="left:0;top:1080px" width="1200" height="500" viewBox="0 0 1200 500">
  <path d="M0 20 C 200 -10 380 50 600 40 C 820 30 1000 -5 1200 30 L1200 500 L0 500 Z" fill="var(--navy)"/>
</svg>
<div class="ph" role="img" aria-label="Faint dotted world map behind the section" style="left:640px;top:1150px;width:520px;height:330px;background:radial-gradient(ellipse at center,rgba(255,255,255,.05),rgba(255,255,255,0) 70%)"></div>
<h2 class="section-title" style="left:146px;top:1218px;color:#d6d7dc">Why Use <span class="accent">A Prep 3PL?</span></h2>
<div class="rule" style="left:150px;top:1267px"></div>
<ul class="abs why-list">
  <li>Work from anywhere in the world.</li>
  <li>Don't have to manage employees, health insurance plans, payroll, sick calls, etc.</li>
  <li>Don't get locked into a 3-5 year warehouse lease where you guarantee hundreds of thousands of dollars</li>
  <li>Grow Your Business Without Commitment</li>
</ul>
<svg class="abs" style="left:720px;top:1160px" width="360" height="360">
  <circle cx="180" cy="180" r="165" fill="none" stroke="var(--yellow)" stroke-width="1.5"/>
</svg>
<div class="ph" role="img" aria-label="Warehouse aisle with a pallet and boxes" style="left:722px;top:1176px;width:148px;height:148px;border-radius:50%;background:linear-gradient(135deg,#b24b3d,#8a8a8a);border:4px solid #fff"></div>
<div class="ph" role="img" aria-label="Hand holding a pen over a signed contract" style="left:858px;top:1295px;width:92px;height:92px;border-radius:50%;background:linear-gradient(135deg,#f0ece2,#d8c48a);border:4px solid #fff"></div>
<div class="ph" role="img" aria-label="Person working at a laptop in a bright home office" style="left:934px;top:1361px;width:150px;height:150px;border-radius:50%;background:linear-gradient(135deg,#d9dcd6,#8f9a86);border:4px solid #fff"></div>
<div class="orbit-label" style="left:900px;top:1246px">Work From<br>Anywhere</div>
<div class="orbit-label" style="left:792px;top:1398px">Without<br>Commitment</div>

<!-- FEATURES (YELLOW) -->
<svg class="abs" style="left:0;top:1550px" width="1200" height="610" viewBox="0 0 1200 610">
  <path d="M0 90 C 250 -10 480 0 620 5 C 860 15 1020 30 1200 60 L1200 610 L0 610 Z" fill="var(--yellow)"/>
  <path d="M265 610 A 340 340 0 0 1 935 610" fill="none" stroke="var(--navy)" stroke-width="1.2" stroke-dasharray="5 5" transform="translate(0,-10)"/>
</svg>
<h2 class="section-title" style="left:0;width:1200px;text-align:center;top:1625px;color:#fbe08a">Why Use <span style="color:#fff">A Prep 3PL?</span></h2>
<div class="feature-text" style="left:0;width:1200px;text-align:center;top:1700px">No Receiving Fees</div>

<div class="feature-icon" style="left:561px;top:1740px"><svg width="44" height="44"><circle cx="22" cy="22" r="17" fill="none" stroke="var(--navy)" stroke-width="2"/><rect x="12" y="16" width="20" height="12" fill="none" stroke="var(--navy)" stroke-width="2"/><line x1="10" y1="34" x2="34" y2="10" stroke="var(--navy)" stroke-width="2"/></svg></div>
<div class="feature-icon" style="left:346px;top:1819px"><svg width="44" height="44"><rect x="18" y="6" width="20" height="26" rx="2" fill="none" stroke="var(--navy)" stroke-width="2"/><path d="M23 20 l4 4 7 -9" fill="none" stroke="var(--navy)" stroke-width="2"/><path d="M6 38 l10 -10 6 2" fill="none" stroke="var(--navy)" stroke-width="2"/></svg></div>
<div class="feature-icon" style="left:767px;top:1819px"><svg width="44" height="44"><path d="M16 40 V20 a3 3 0 0 1 6 0 V28 h10 a4 4 0 0 1 4 4 V40" fill="none" stroke="var(--navy)" stroke-width="2"/><circle cx="26" cy="12" r="8" fill="none" stroke="var(--navy)" stroke-width="2"/></svg></div>
<div class="feature-icon" style="left:247px;top:1958px"><svg width="44" height="44"><path d="M8 18 L22 11 L36 18 L22 25 Z M8 18 V32 L22 39 L36 32 V18 M22 25 V39" fill="none" stroke="var(--navy)" stroke-width="2"/><circle cx="22" cy="7" r="4" fill="none" stroke="var(--navy)" stroke-width="2"/></svg></div>
<div class="feature-icon" style="left:877px;top:1958px"><svg width="44" height="44"><rect x="12" y="4" width="20" height="36" rx="3" fill="none" stroke="var(--navy)" stroke-width="2"/><rect x="16" y="16" width="16" height="11" fill="none" stroke="var(--navy)" stroke-width="2"/><path d="M16 16 l8 6 8 -6" fill="none" stroke="var(--navy)" stroke-width="2"/></svg></div>

<div class="feature-text" style="left:160px;top:1825px;width:160px;text-align:right">48 Hour Turn Around Guarantee Done in 48 Hours or Its Free</div>
<div class="feature-text" style="left:866px;top:1825px;width:170px">No Monthly Subscription Only Pay For What You Use</div>
<div class="feature-text" style="left:100px;top:1975px;width:126px;text-align:right">No Pallet Or Outbound Fees</div>
<div class="feature-text" style="left:976px;top:1975px;width:140px">Email And Phone Support</div>
<div class="ph" role="img" aria-label="Smiling woman in a yellow sweater giving two thumbs up" style="left:505px;top:1844px;width:190px;height:309px;border-radius:95px 95px 0 0;background:linear-gradient(180deg,#3a2a22 0%,#7a5238 35%,#e9a21c 60%,#f0a81e 100%)"></div>

<!-- SOFTWARE -->
<svg class="abs" style="left:0;top:2150px" width="1200" height="460" viewBox="0 0 1200 460">
  <path d="M0 0 H1200 V400 C 900 480 300 440 0 400 Z" fill="var(--mist)"/>
</svg>
<svg class="abs" style="left:97px;top:2224px" width="480" height="320">
  <path d="M70 100 H10 V170" fill="none" stroke="var(--yellow)" stroke-width="3"/>
  <path d="M440 200 H476 V270 H440" fill="none" stroke="var(--yellow)" stroke-width="3"/>
</svg>
<div class="shot" style="left:156px;top:2224px;width:255px;height:140px"><div class="shot-side"></div></div>
<div class="shot" style="left:323px;top:2281px;width:215px;height:120px"><div class="shot-side" style="width:30px"></div></div>
<div class="ph" role="img" aria-label="Shipping containers stacked at a port at sunset" style="left:97px;top:2380px;width:152px;height:160px;background:linear-gradient(160deg,#e7a35b,#8a3b2c 55%,#3c3b48)"></div>
<div class="shot" style="left:249px;top:2380px;width:60px;height:160px"></div>
<div class="shot" style="left:323px;top:2418px;width:215px;height:122px"><div class="shot-side" style="width:30px"></div></div>

<h2 class="section-title" style="left:680px;top:2256px">Our <span class="accent">Software</span></h2>
<div class="rule" style="left:682px;top:2303px"></div>
<p class="abs software-copy">Know What Inventory Is At Our Warehouse In Real Time. Our Software Allows You To Track Your Inventory And Know How Your Shipment Status In Real Time. Professional Software Designed Specifically For Our Needs.</p>
<div class="btn" style="left:680px;top:2440px;width:183px;height:37px;font-size:13px">Download Now !</div>
<div class="btn" style="left:874px;top:2440px;width:180px;height:37px;font-size:13px;background:#a9a9ab;color:var(--navy)">Get a Free Trial</div>

<!-- PRICING -->
<h2 class="section-title" style="left:0;width:1200px;text-align:center;top:2682px">Our <span class="accent">Pricing</span></h2>
<div class="rule" style="left:571px;top:2730px"></div>
<svg class="abs" style="left:160px;top:2820px" width="920" height="340">
  <defs><linearGradient id="frameFade" x1="0" x2="1"><stop offset="0" stop-color="#1c1e2b"/><stop offset="1" stop-color="#c49a1a"/></linearGradient></defs>
  <path d="M16 70 V14 H426" fill="none" stroke="url(#frameFade)" stroke-width="16"/>
  <path d="M16 250 V316 H426" fill="none" stroke="url(#frameFade)" stroke-width="16"/>
  <path d="M845 14 H885 V316 H845" fill="none" stroke="var(--yellow)" stroke-width="11"/>
</svg>
<div class="abs pricing-lead">Running a Brindlemart<br>Business?</div>
<p class="abs pricing-sub">Let us streamline your business by saving you time and money.</p>
<div class="abs price-card">
  <div style="position:absolute;left:0;top:20px;width:419px">
    <div class="price-row" style="top:0">≤20 units per item<span class="amt">$1.40</span></div>
    <div class="price-row" style="top:42px">&gt;20 units per item<span class="amt">$1.20</span></div>
    <div class="price-row" style="top:84px">Bundle/Multipack Up To 4 Items<span class="amt">$5.50</span></div>
    <div class="price-row" style="top:126px">Bundle/Multipack 5-8 Items<span class="amt">$4.00</span></div>
    <div class="price-row" style="top:168px">Storage - 1 Pallet Or One Shelving unit<span class="amt">$25/mo</span></div>
    <div class="price-row" style="top:210px">Special Prep (glass/fragile) Per Item<span class="amt">$1.00</span></div>
    <div class="price-row" style="top:252px">Oversize Surcharge per item<span class="amt">$0.50</span></div>
  </div>
  <div class="btn" style="left:134px;top:345px;width:152px;height:38px;font-size:13px">Inquiry Now</div>
</div>

<!-- GUARANTEE -->
<div class="ph" role="img" aria-label="Faint dotted world map" style="left:260px;top:3330px;width:440px;height:330px;background:radial-gradient(ellipse at center,rgba(0,0,0,.035),rgba(0,0,0,0) 70%)"></div>
<h2 class="section-title" style="left:124px;top:3322px">Our <span class="accent">Guarantee</span></h2>
<div class="rule" style="left:126px;top:3370px"></div>
<div class="guarantee-copy abs">
  <p>All Orders Will be Prepped and Ready For Shipment In 48 Business Hours (often 24 or less) and We Guarantee It.</p>
  <p style="margin-top:8px">We are confident in our services and if we do not fulfill our obligation</p>
</div>
<div class="abs guarantee-big">We Offer A 500 Item<br><span class="muted">(Up To $700)</span></div>
<div class="abs guarantee-note">Credit on Your Next Shipment.</div>
<div class="btn" style="left:126px;top:3680px;width:146px;height:38px;font-size:13px">Get Started</div>
<svg class="abs" style="left:670px;top:3290px" width="420" height="420">
  <path d="M 40 210 A 170 170 0 0 1 380 210" fill="none" stroke="var(--yellow)" stroke-width="14" transform="rotate(-20 210 210)"/>
  <path d="M 380 210 A 170 170 0 0 1 40 210" fill="none" stroke="#b5b5b5" stroke-width="8" transform="rotate(-20 210 210)"/>
</svg>
<div class="ph" role="img" aria-label="Courier walking a bicycle with a yellow delivery backpack" style="left:703px;top:3323px;width:354px;height:354px;border-radius:50%;background:linear-gradient(135deg,#9c9d9f,#c9c8c4 50%,#6a6b6e)"></div>

<!-- CONTACT -->
<div class="abs" style="left:0;top:3828px;width:1200px;height:500px;background:var(--yellow)"></div>
<div class="ph" role="img" aria-label="Faint dotted world map" style="left:300px;top:3860px;width:600px;height:300px;background:radial-gradient(ellipse at center,rgba(255,255,255,.14),rgba(255,255,255,0) 70%)"></div>
<h2 class="section-title" style="left:0;width:1200px;text-align:center;top:3898px;color:#fbe08a">Contact <span style="color:#fff">Us</span></h2>
<div class="rule" style="left:571px;top:3946px"></div>
<p class="abs contact-sub">Have an any Question Please Contact us Today !</p>
<div class="field select" style="left:187px;top:4015px;width:262px">Company name*</div>
<div class="field" style="left:457px;top:4015px;width:262px">Name *</div>
<div class="field" style="left:726px;top:4015px;width:287px;height:92px">How Can We Help You?</div>
<div class="field" style="left:187px;top:4068px;width:262px">Email *</div>
<div class="field select" style="left:457px;top:4068px;width:262px">Describe Yourself? *</div>
<div class="btn" style="left:543px;top:4124px;width:112px;height:37px;font-size:13px;border:2px solid var(--navy);background:transparent">Submit</div>

<!-- FOOTER -->
<svg class="abs" style="left:0;top:4250px" width="1200" height="569" viewBox="0 0 1200 569">
  <path d="M0 180 C 300 40 700 20 1200 60 L1200 569 L0 569 Z" fill="var(--navy)"/>
  <path d="M1200 45 C 1150 50 1100 55 1050 60 C 1110 70 1160 85 1200 100 Z" fill="var(--yellow)"/>
  <path d="M0 150 C 30 140 50 130 80 118 C 50 140 25 160 0 185 Z" fill="var(--yellow)"/>
</svg>
<div class="brand" style="left:0;width:1200px;text-align:center;top:4357px;font-size:30px;letter-spacing:5px">ORBITLINE 3PL</div>

<div class="contact-item" style="left:210px">
  <div class="contact-ring"><svg width="22" height="26"><path d="M11 25 C 4 16 2 12 2 9 a9 9 0 0 1 18 0 c0 3 -2 7 -9 16z" fill="var(--navy)"/><circle cx="11" cy="9" r="3.5" fill="var(--yellow)"/></svg></div>
  <div class="contact-lines">ORBITLINE 3PL<span>101 - Lorem ipsum simple<br>text print industry.</span></div>
</div>
<div class="contact-item" style="left:476px">
  <div class="contact-ring"><svg width="24" height="24"><path d="M5 3 l5 0 2 5 -3 2 a11 11 0 0 0 5 5 l2 -3 5 2 0 5 a15 15 0 0 1 -16 -16z" fill="var(--navy)"/></svg></div>
  <div class="contact-lines">Phone :<span>+1 000 000 0000</span></div>
</div>
<div class="contact-item" style="left:750px">
  <div class="contact-ring"><svg width="24" height="24"><rect x="3" y="6" width="18" height="13" fill="var(--navy)"/><path d="M3 6 L12 13 L21 6" stroke="var(--yellow)" stroke-width="1.5" fill="none"/></svg></div>
  <div class="contact-lines">Email :<span>info@orbitline3pl.com</span></div>
</div>

<div class="abs copyright">©Orbitline3PL - 2021 All rights reserved.</div>
<div class="abs disclaimer-title">Disclaimer</div>
<p class="abs disclaimer">* Our guarantee is 48 hours from the time an outbound shipment is created in our system. Weekends and holidays excluded. Orders created on a friday after hours, Saturday or Sunday will be counted from the open of business on Monday morning. We offer a credit of up to 500 units on your next shipment. These credits are for standard prep items only, no bundles, bubble wrapped or multipack units. Outbound shipments will be prepped and ready to ship. We are unable to control shipping companies and freight carriers. Orders after daily pickups are completed will be ready for next day pickup.</p>

</body>
</html>
```